StoneBay construction business cards

I need a business card with a replacement window photo or graphic on it .phone # 919 482 -7316 stonebayconstruction@mailfort.net fax #919 274-8093 '' The Window Replacement Specialist"

Industry/Entity Type

Construction

```html
<!DOCTYPE html>
<html lang="en">
<head>
<meta charset="utf-8">
<title>StoneBay Construction – Business Cards</title>
<link rel="stylesheet" href="https://fonts.googleapis.com/css2?family=Josefin+Sans:wght@400;700&display=swap">
<style>
  :root {
    --backdrop: #efece6;
    --lime: #55fb06;
    --forest: #2e8a12;
    --leaf: #3fb51a;
    --paper: #ffffff;
    --ink-light: #ffffff;
    --shadow: rgba(60, 45, 25, 0.22);
  }
  * { margin: 0; padding: 0; box-sizing: border-box; }
  html, body {
    width: 1200px; height: 1000px; overflow: hidden;
    background: var(--backdrop);
    font-family: "Josefin Sans", sans-serif;
  }
  .canvas { position: relative; width: 1200px; height: 1000px; }
  .card {
    position: absolute; left: 290px; width: 620px; height: 354px;
    box-shadow: 0 10px 26px var(--shadow);
  }
  .card--front { top: 100px; background: var(--lime); color: var(--ink-light); }
  .card--back  { top: 546px; background: var(--paper); color: var(--lime); }

  .brand { position: absolute; left: 44px; top: 58px; width: 320px; }
  .brand__name { font-weight: 700; font-size: 54px; line-height: 1; letter-spacing: 1px; }
  .brand__sub { font-weight: 700; font-size: 20px; letter-spacing: 3px; margin: 6px 0 0 70px; }
  .tagline {
    display: inline-block; margin-top: 16px; padding: 7px 0 5px;
    border-top: 2px solid currentColor; border-bottom: 2px solid currentColor;
    font-weight: 400; font-size: 14px; letter-spacing: 0.3px; white-space: nowrap;
  }
  .contacts {
    position: absolute; left: 44px; top: 236px; list-style: none;
    font-size: 14px; line-height: 1;
  }
  .contacts li { display: flex; align-items: center; gap: 12px; margin-bottom: 10px; }
  .contacts svg { width: 15px; height: 15px; flex: none; }

  .window-graphic {
    position: absolute; right: 44px; top: 40px; width: 200px; height: 250px;
  }
  .card--front .window-graphic { background: linear-gradient(160deg, var(--forest), #3d9e1a); }
  .card--back .window-graphic { background: linear-gradient(160deg, var(--leaf), var(--forest)); }
</style>
</head>
<body>
<main class="canvas">

  <section class="card card--front" aria-label="Business card front">
    <div class="brand">
      <div class="brand__name">StoneBay</div>
      <div class="brand__sub">Construction</div>
      <div class="tagline">THE WINDOW REPLACEMENT SPECIALIST</div>
    </div>

    <ul class="contacts">
      <li>
        <svg viewBox="0 0 16 16" aria-hidden="true"><path fill="currentColor" d="M3.6 1.5l2.3 2.6-1.2 1.7c.9 2 2.4 3.5 4.4 4.4l1.7-1.2 2.6 2.3-1.4 2.3C6.7 13.4 2.6 9.3 1.3 2.9z"/></svg>
        <span>#919 482 -7316</span>
      </li>
      <li>
        <svg viewBox="0 0 16 16" aria-hidden="true"><path fill="currentColor" d="M4 1h8v4H4zM1 6h14v7h-3v2H4v-2H1zm4 5v3h6v-3z"/></svg>
        <span>#919 274-8093</span>
      </li>
      <li>
        <svg viewBox="0 0 16 16" aria-hidden="true"><path fill="currentColor" d="M1 3h14v10H1zm1.5 1.2v.4L8 9l5.5-4.4v-.4z"/></svg>
        <span>stonebayconstruction@mailfort.net</span>
      </li>
    </ul>

    <div class="window-graphic" role="img" aria-label="Graphic of a six-pane replacement window in a green frame"></div>
  </section>

  <section class="card card--back" aria-label="Business card back">
    <div class="brand">
      <div class="brand__name">StoneBay</div>
      <div class="brand__sub">Construction</div>
      <div class="tagline">THE WINDOW REPLACEMENT SPECIALIST</div>
    </div>

    <div class="window-graphic" role="img" aria-label="Outline graphic of a six-pane replacement window"></div>
  </section>

</main>
</body>
</html>
```